Thornquist Landscaping buisness cards.

There's no existing logo andthis is a new landscaping buisness looking for a complete card design. Would like the logo and name to take up one side.

Target Market(s)

Professionals, Middle aged, Elderly.

Industry/Entity Type

Landscaping

Contact Information for Business Card

Thornquist Landscaping
Malcolm Thornquist (owner)
555-782-4610
Malcolmrthornquist@fernmail.example

Font styles to use
Sans Serif

Colors
9bcb3c
0555a3
ec1f27

Requirements
Must have
• Easy to read print and contact information, all capital letters
Nice to have
• Colored backdrop
Should not have
• Pictures of lawnmowers.

```html
<!DOCTYPE html>
<html lang="en">
<head>
<meta charset="UTF-8">
<title>Thornquist Landscaping – Business Cards</title>
<link href="https://fonts.googleapis.com/css2?family=Lato:wght@400;700&display=swap" rel="stylesheet">
<style>
  :root {
    --leaf-green: #8cc63f;
    --leaf-light: #a9d65f;
    --leaf-deep: #6fa832;
    --ink-grey: #4a4a4a;
    --paper: #ffffff;
    --backdrop: #ecebe6;
  }
  * { margin: 0; padding: 0; box-sizing: border-box; }
  html, body {
    width: 1200px; height: 1024px; overflow: hidden;
    background: var(--backdrop);
    font-family: "Lato", Arial, sans-serif;
  }
  .card {
    position: absolute; left: 260px;
    width: 680px; height: 388px;
    border-radius: 4px; overflow: hidden;
    box-shadow: 0 6px 20px rgba(0,0,0,0.15);
  }
  .card--front { top: 90px; background: var(--paper); }
  .card--back { top: 546px; background: var(--leaf-green); }

  /* Front */
  .front-leaves {
    position: absolute; right: -30px; top: -40px;
    width: 330px; height: 190px;
    border-radius: 0 0 0 190px;
    background: linear-gradient(135deg, var(--leaf-light), var(--leaf-green));
  }
  .front-brand {
    position: absolute; left: 44px; top: 96px;
    display: flex; align-items: center; gap: 12px;
    color: var(--leaf-green); font-weight: 700;
  }
  .brand-dot {
    width: 26px; height: 26px; border-radius: 50%;
    background: var(--leaf-green);
  }
  .front-brand .brand-name { font-size: 30px; letter-spacing: 1px; line-height: 1; }
  .front-brand .brand-sub { font-size: 30px; letter-spacing: 1px; line-height: 1.1; }
  .person {
    position: absolute; left: 44px; top: 210px;
  }
  .person-name {
    color: var(--leaf-green); font-weight: 700; font-size: 22px; letter-spacing: 0.5px;
  }
  .person-role {
    color: var(--ink-grey); font-size: 14px; letter-spacing: 1px; margin-top: 4px;
  }
  .contact {
    position: absolute; left: 44px; top: 284px;
    list-style: none;
  }
  .contact li {
    display: flex; align-items: center; gap: 10px;
    color: var(--ink-grey); font-size: 17px; letter-spacing: 0.3px;
    margin-bottom: 10px;
  }
  .contact .phone { font-size: 22px; font-weight: 700; }
  .contact-icon {
    width: 20px; height: 20px; border-radius: 50%;
    background: var(--leaf-green);
    display: flex; align-items: center; justify-content: center;
  }

  /* Back */
  .back-leaves {
    position: absolute; right: -60px; top: -40px;
    width: 420px; height: 470px;
    border-radius: 60% 40% 50% 50%;
    background: radial-gradient(ellipse at 40% 40%, rgba(111,168,50,0.55), rgba(140,198,63,0));
  }
  .back-brand {
    position: absolute; left: 0; right: 0; top: 0; bottom: 0;
    display: flex; flex-direction: column; align-items: center; justify-content: center;
    color: var(--paper); font-weight: 700; letter-spacing: 3px;
  }
  .back-brand .brand-name { font-size: 54px; line-height: 1; }
  .back-brand .brand-sub { font-size: 54px; line-height: 1.1; }
</style>
</head>
<body>

  <section class="card card--front">
    <div class="front-leaves" role="img" aria-label="Green leaf illustration"></div>

    <div class="front-brand">
      <span class="brand-dot"></span>
      <div>
        <div class="brand-name">THORNQUIST</div>
        <div class="brand-sub">LANDSCAPING</div>
      </div>
    </div>

    <div class="person">
      <div class="person-name">MALCOLM THORNQUIST</div>
      <div class="person-role">OWNER</div>
    </div>

    <ul class="contact">
      <li class="phone">
        <span class="contact-icon">
          <svg width="12" height="12" viewBox="0 0 24 24"><path fill="#fff" d="M6.6 10.8a15.1 15.1 0 0 0 6.6 6.6l2.2-2.2a1 1 0 0 1 1-.25 11.4 11.4 0 0 0 3.6.57 1 1 0 0 1 1 1V20a1 1 0 0 1-1 1A17 17 0 0 1 3 4a1 1 0 0 1 1-1h3.5a1 1 0 0 1 1 1c0 1.25.2 2.45.57 3.57a1 1 0 0 1-.25 1z"/></svg>
        </span>
        555-782-4610
      </li>
      <li class="email">
        <span class="contact-icon">
          <svg width="12" height="12" viewBox="0 0 24 24"><rect x="3" y="6" width="18" height="12" rx="1" fill="none" stroke="#fff" stroke-width="2"/><path d="M3 7l9 6 9-6" fill="none" stroke="#fff" stroke-width="2"/></svg>
        </span>
        MALCOLMRTHORNQUIST@FERNMAIL.EXAMPLE
      </li>
    </ul>
  </section>

  <section class="card card--back">
    <div class="back-leaves" role="img" aria-label="Faint large leaf decoration"></div>
    <div class="back-brand">
      <div class="brand-name">THORNQUIST</div>
      <div class="brand-sub">LANDSCAPING</div>
    </div>
  </section>

</body>
</html>
```